Make my current Presentation more Professional

I am selling frozen pulp and sorbets. I have a presentation done to introduce the product to customers i want to sell my product to. However the presentation does not have a character - i need to make it look more professional, and at the same time i want to make the product stand out, and have the overall presentation look very fresh, and embedding the true look and feel of what we are offering. 100% NATURAL TROPICAL BRAZILIAN FRUITS.
Some of the text in the presentation is pasted like image, i need it as text.
There should be a specific template that you will use so that i can add remove slides later on according to my requirement

Target Market(s)

Presentation is intended for F&B managers & Chefs in hotels, restaurant

Industry/Entity Type

Food Service

Font styles to use
Sans Serif

Colors

Designer to choose colors to be used in the design.

Requirements
Must have
• A fresh, natural look and feel of tropical fruits.
• It also should come across professional as we are selling products to potential customers.
• I need a clear template - with header, font etc..
Nice to have
• If you want to buy some pictures of fruits, i can buy it for you to make it look great

```html
<!DOCTYPE html>
<html lang="en">
<head>
<meta charset="utf-8">
<title>Pomar Tropical – Presentation Template</title>
<link href="https://fonts.googleapis.com/css2?family=Lato:wght@700;900&family=Bitter:wght@600;700&display=swap" rel="stylesheet">
<style>
  :root {
    --brand-green: #047a22;
    --label-green: #0b5b14;
    --lime: #9cc200;
    --deep-green: #0d4a12;
    --deep-green-2: #1f6b1a;
    --yellow: #ffdd00;
    --white: #ffffff;
    --heading-green: #0b4d12;
  }
  * { box-sizing: border-box; margin: 0; padding: 0; }
  html, body { width: 1200px; height: 1200px; overflow: hidden; background: var(--white); }
  .sheet { position: relative; width: 1200px; height: 1200px; font-family: 'Lato', sans-serif; }

  .row-label {
    position: absolute; right: 800px; width: 360px;
    text-align: right; color: var(--label-green);
    font-family: 'Lato', sans-serif; font-weight: 900;
    font-size: 58px; line-height: 70px; letter-spacing: 0.5px;
  }

  .slide { position: absolute; left: 446px; width: 671px; height: 377px; overflow: hidden; }
  .block { position: absolute; }

  /* title slide */
  .title-slide { top: 18px; background: var(--brand-green); }
  .title-photo {
    left: 214px; top: 0; width: 457px; height: 377px;
    background:
      radial-gradient(circle at 20% 35%, #f39a1c 0, transparent 30%),
      radial-gradient(circle at 80% 30%, #f7d23a 0, transparent 28%),
      radial-gradient(circle at 45% 20%, #c9a24a 0, transparent 30%),
      radial-gradient(circle at 30% 88%, #8fb83a 0, transparent 28%),
      radial-gradient(circle at 75% 90%, #e0672a 0, transparent 30%),
      linear-gradient(160deg, #fbeed6, #f6c774 55%, #e8a03c);
  }
  .brand-box {
    left: 37px; top: 213px; width: 177px; height: 82px;
    background: var(--white);
    display: flex; align-items: center; justify-content: center; gap: 8px;
  }
  .brand-dot { width: 16px; height: 16px; border-radius: 50%; background: var(--brand-green); }
  .brand-name { font-family: 'Lato', sans-serif; font-weight: 900; font-size: 19px; color: var(--brand-green); }
  .title-band {
    left: 214px; top: 213px; width: 457px; height: 82px;
    background: var(--brand-green); color: var(--white); text-align: center;
  }
  .title-band h1 {
    font-family: 'Bitter', serif; font-weight: 700; font-size: 43px; line-height: 1;
    margin-top: 5px; letter-spacing: 0.5px;
  }
  .title-band p { font-family: 'Lato', sans-serif; font-weight: 700; font-size: 22px; margin-top: 4px; }

  /* content slides */
  .lime { background: var(--lime); }
  .dark-photo {
    background:
      radial-gradient(circle at 30% 30%, #2f7a22 0, transparent 35%),
      radial-gradient(circle at 70% 75%, #246a1b 0, transparent 35%),
      linear-gradient(150deg, var(--deep-green-2), var(--deep-green) 60%, #0a3b0e);
  }
  .yellow-square { position: absolute; width: 51px; height: 50px; background: var(--yellow); }

  .col-heading {
    position: absolute; font-family: 'Bitter', serif; font-weight: 700;
    font-size: 29px; color: var(--heading-green); line-height: 1;
  }
  .points { position: absolute; list-style: none; color: var(--white); font-weight: 700; font-size: 13.4px; line-height: 17px; }
  .points li { position: relative; padding-left: 14px; margin-bottom: 16px; }
  .points li::before {
    content: ""; position: absolute; left: 0; top: 6px; width: 5px; height: 5px;
    border-radius: 50%; background: var(--white);
  }

  .stat { position: absolute; color: var(--white); font-family: 'Bitter', serif; font-weight: 700; }
  .stat-number { font-size: 64px; line-height: 1; }
  .stat-number .hash { font-size: 40px; vertical-align: 14px; margin-right: 4px; }
  .stat-caption { font-size: 18px; line-height: 18px; margin-top: 6px; }

  .claim { position: absolute; color: var(--white); font-family: 'Bitter', serif; font-weight: 700; }
  .claim h2 { font-size: 36px; line-height: 1; }
  .claim li { list-style: none; font-size: 19px; line-height: 33px; margin-left: 14px; }
  .claim ul { margin-top: 12px; }
</style>
</head>
<body>
<div class="sheet">

  <div class="row-label" style="top:152px;">TITLE<br>SLIDE</div>
  <div class="row-label" style="top:520px;">2 COLUMN<br>SLIDE</div>
  <div class="row-label" style="top:912px;">1 COLUMN<br>SLIDE</div>

  <!-- Title slide -->
  <section class="slide title-slide">
    <div class="block title-photo" role="img" aria-label="Tropical fruit juices, pineapple, mango, sorbet scoops and fresh fruits"></div>
    <div class="block brand-box">
      <span class="brand-dot"></span>
      <span class="brand-name">Pomar Tropical</span>
    </div>
    <div class="block title-band">
      <h1>Concept Brief</h1>
      <p>Harbor City International Airport HCX</p>
    </div>
  </section>

  <!-- Two column slide -->
  <section class="slide lime" style="top:413px;">
    <h2 class="col-heading" style="left:34px; top:26px;">Advantages</h2>
    <ul class="points" style="left:18px; top:82px; width:210px;">
      <li>Lorem ipsum dolor sit amet, consectetur adipiscing elit.</li>
      <li>Morbi ultricies molestie orci.</li>
      <li>Aenean purus mauris, sodales nec diam dignissim, porttitor laoreet enim.</li>
      <li>Aliquam id sollicitudin turpis. Vivamus aliquet elit sem, et ornare ex aliquam in.</li>
    </ul>
    <h2 class="col-heading" style="left:262px; top:26px;">Major points</h2>
    <ul class="points" style="left:248px; top:82px; width:215px;">
      <li>In cursus, felis non pretium molestie, tellus lacus facilisis metus, ut accumsan nisi nulla accumsan risus.</li>
      <li>Fusce placerat risus sit amet lectus egestas, pretium porttitor nisi facilisis.</li>
      <li>Nulla interdum viverra. Nam suscipit, eros ut vulputate ultrices.</li>
      <li>Nec varius felis odio ut mi. Sed felis nisl, congue at finibus in, porttitor ut elit.</li>
    </ul>
    <div class="block dark-photo" style="left:475px; top:0; width:196px; height:377px;" role="img" aria-label="Tropical fruits and leaves in deep green tone"></div>
    <div class="yellow-square" style="left:620px; top:13px;"></div>
    <div class="stat" style="left:535px; top:132px;">
      <div class="stat-number"><span class="hash">#</span>1</div>
      <div class="stat-caption">in world<br>surveys</div>
    </div>
  </section>

  <!-- One column slide -->
  <section class="slide lime" style="top:805px;">
    <div class="block dark-photo" style="left:0; top:0; width:357px; height:377px;" role="img" aria-label="Heap of tropical fruits including watermelon in deep green tone"></div>
    <div class="yellow-square" style="left:0; top:17px;"></div>
    <div class="claim" style="left:80px; top:84px;">
      <h2>100% fruit!</h2>
      <ul>
        <li>no preservatives</li>
        <li>no colorings</li>
        <li>no sugar added</li>
      </ul>
    </div>
    <h2 class="col-heading" style="left:421px; top:26px;">Major points</h2>
    <ul class="points" style="left:407px; top:82px; width:215px;">
      <li>In cursus, felis non pretium molestie, tellus lacus facilisis metus, ut accumsan nisi nulla accumsan risus.</li>
      <li>Fusce placerat risus sit amet lectus egestas, pretium porttitor nisi facilisis.</li>
      <li>Nulla interdum viverra. Nam suscipit, eros ut vulputate ultrices.</li>
      <li>Nec varius felis odio ut mi. Sed felis nisl, congue at finibus in, porttitor ut elit.</li>
    </ul>
  </section>

</div>
</body>
</html>
```